A Weather Forecasting Site needs designs

We need a website design for our new venture which is a weather forecasting website. This website should have the latest design trends.

Menu
Weather, Maps, Videos and Photos

The home page requirements are as follows:
- Search Bar
- Local Weather
- Weather forecast of major cities in the World
Favorite locations
- Space for ADs
- Email signup

Weather Details page
This page will be redirected from the home page when you click on any of the weather forecast section

We are open to all kinds of designs and ideas. Feel free to you colors which suite your design.

```html
<!DOCTYPE html>
<html lang="en">
<head>
<meta charset="utf-8">
<title>Skyvane – Weather Forecasting</title>
<link href="https://fonts.googleapis.com/css2?family=Open+Sans:wght@400;600;700&family=Raleway:wght@700;800&display=swap" rel="stylesheet">
<style>
:root{
  --blue:#1f6db8;
  --blue-band:#1b6cb8;
  --orange:#f6922a;
  --ink:#333;
  --muted:#777;
  --line:#e3e3e3;
  --page:#f5f5f5;
  --white:#fff;
  --nav:#f7f7f7;
}
*{margin:0;padding:0;box-sizing:border-box}
html,body{width:672px;height:1200px;overflow:hidden}
body{font-family:"Open Sans",sans-serif;color:var(--ink);background:var(--page);position:relative}
.abs{position:absolute}
.header{left:0;top:0;width:672px;height:58px;background:var(--white)}
.brand{left:74px;top:24px;display:flex;align-items:center;gap:6px;font-weight:700;font-size:16px;color:#222}
.brand-dot{width:16px;height:16px;border-radius:50%;background:var(--blue)}
.btn{background:var(--orange);color:var(--white);font-weight:600;text-transform:uppercase;display:flex;align-items:center;justify-content:center}
.view-maps{left:535px;top:15px;width:63px;height:28px;font-size:7px;gap:3px}
.nav{left:0;top:58px;width:672px;height:30px;background:var(--nav);border-top:1px solid var(--line);border-bottom:1px solid var(--line)}
.nav-item{top:0;height:29px;display:flex;align-items:center;justify-content:center;font-size:7.5px;font-weight:600;color:#333;border-right:1px solid var(--line)}
.nav-item.active{background:var(--white);color:var(--blue);border-top:3px solid var(--blue);border-left:1px solid var(--line)}
.hero{left:0;top:88px;width:672px;height:242px;background:linear-gradient(180deg,#4a4540 0%,#5e4a3a 45%,#3b3229 75%,#262420 100%)}
.hero-title{left:0;top:155px;width:672px;text-align:center;font-family:"Raleway",sans-serif;font-weight:800;font-size:22px;color:var(--white)}
.hero-sub{left:146px;top:187px;width:380px;text-align:center;font-size:7.8px;line-height:14px;color:#eee}
.arrow{top:202px;width:15px;height:15px;border-radius:50%;background:rgba(255,255,255,.35);display:flex;align-items:center;justify-content:center}
.search{left:167px;top:232px;width:337px;height:28px;border:1px solid rgba(255,255,255,.8);display:flex}
.search-field{flex:1;display:flex;align-items:center;padding-left:10px;font-size:6.5px;font-weight:700;color:var(--white)}
.search-btn{width:63px;font-size:7.5px;gap:4px}
.card{background:var(--white);border:1px solid #ddd}
.map{background:linear-gradient(135deg,#e4e2dc,#d9d7cf 50%,#e8e6de)}
.section-title{font-family:"Raleway",sans-serif;font-weight:700;font-size:9px;color:var(--blue);text-transform:uppercase}
.lw-item{left:272px;width:160px;height:54px;border-bottom:1px solid var(--line);display:flex;gap:8px}
.lw-item:last-child{border-bottom:0}
.icon{width:22px;height:22px;border-radius:50%;border:1px solid #ddd;display:flex;align-items:center;justify-content:center;flex:none;background:var(--white)}
.temp{font-size:10px;font-weight:700;color:var(--orange)}
.temp sup{font-size:7px}
.city{font-size:6.5px;color:#444;font-weight:400}
.lw-text{font-size:5.6px;color:var(--muted);line-height:10.5px}
.ad{left:450px;top:362px;width:148px;height:191px;background:radial-gradient(ellipse at 70% 55%,#2c2c2e 0%,#111 55%,#000 100%)}
.ad-top{left:11px;top:16px;font-size:6.6px;font-weight:600;color:var(--white);line-height:12px}
.ad-bottom{left:11px;top:141px;font-size:6.5px;font-weight:600;color:var(--white);display:flex;align-items:baseline;gap:2px}
.ad-bottom b{font-size:12px;color:var(--orange)}
.ad-btn{left:11px;top:162px;width:50px;height:15px;font-size:6.5px}
.city-cell{height:36px;width:107px;display:flex;align-items:center;gap:6px;border-right:1px solid var(--line)}
.fav-img{top:922px;width:117px;height:82px}
.fav-cap{top:1010px;width:117px;text-align:center;font-size:6.3px;color:#222}
.email{left:0;top:1073px;width:672px;height:71px;background:var(--blue-band)}
.email-title{left:74px;top:15px;font-family:"Raleway",sans-serif;font-weight:700;font-size:13px;color:var(--white)}
.email-sub{left:74px;top:35px;width:275px;font-size:6.4px;line-height:12px;color:#e6eef7}
.email-form{left:360px;top:21px;width:238px;height:29px;border:1px solid rgba(255,255,255,.8);display:flex}
.email-field{flex:1;display:flex;align-items:center;padding-left:10px;font-size:6.3px;color:var(--white)}
.email-btn{width:63px;font-size:7px}
.footer-links{left:74px;top:1161px;font-size:5.4px;color:#333;word-spacing:1px}
.footer-copy{left:74px;top:1174px;font-size:5.2px;color:#555}
.connect{left:472px;top:1168px;font-size:5.2px;color:#333}
.social{top:1162px;width:15px;height:15px;border-radius:50%}
.code{left:615px;top:1167px;font-size:6px;color:#555}
</style>
</head>
<body>
<header class="abs header">
  <div class="abs brand"><span class="brand-dot"></span>Skyvane</div>
  <div class="abs btn view-maps">View Maps
    <svg width="7" height="5" viewBox="0 0 14 10"><ellipse cx="7" cy="5" rx="6.5" ry="4.3" fill="none" stroke="#fff" stroke-width="1.6"/><circle cx="7" cy="5" r="2" fill="#fff"/></svg>
  </div>
</header>

<nav class="abs nav">
  <div class="abs nav-item active" style="left:74px;width:58px;top:-1px;height:30px">HOME</div>
  <div class="abs nav-item" style="left:132px;width:94px">WEATHER</div>
  <div class="abs nav-item" style="left:226px;width:56px">MAPS</div>
  <div class="abs nav-item" style="left:282px;width:80px">VIDEOS</div>
  <div class="abs nav-item" style="left:362px;width:77px">PHOTOS</div>
  <div class="abs nav-item" style="left:439px;width:76px">ABOUT</div>
  <div class="abs nav-item" style="left:515px;width:83px;border-right:0">CONTACT</div>
</nav>

<section class="abs hero" role="img" aria-label="Mountain valley landscape photograph"></section>
<h1 class="abs hero-title">WEATHER FORECASTING</h1>
<p class="abs hero-sub">Lorem ipsum dolor sit amet, consectetur adipiscing elit, sed do eiusmod tempor incididunt ut labore et dolore magna aliqua.enim ad minim veniam, quis nostrud...</p>
<div class="abs arrow" style="left:59px"><svg width="7" height="7" viewBox="0 0 10 10"><path d="M6.5 2 3.5 5l3 3" fill="none" stroke="#fff" stroke-width="1.6"/></svg></div>
<div class="abs arrow" style="left:598px"><svg width="7" height="7" viewBox="0 0 10 10"><path d="M3.5 2l3 3-3 3" fill="none" stroke="#fff" stroke-width="1.6"/></svg></div>
<form class="abs search">
  <div class="search-field">ENTER CITY (or) ZIP CODE</div>
  <div class="btn search-btn">Search
    <svg width="7" height="7" viewBox="0 0 10 10"><circle cx="4.2" cy="4.2" r="3" fill="none" stroke="#fff" stroke-width="1.5"/><path d="M6.5 6.5 9 9" stroke="#fff" stroke-width="1.6"/></svg>
  </div>
</form>

<!-- Local weather -->
<section class="abs card" style="left:74px;top:362px;width:367px;height:191px"></section>
<div class="abs map" style="left:83px;top:370px;width:174px;height:173px" role="img" aria-label="Street map of the local area"></div>
<h2 class="abs section-title" style="left:272px;top:373px">Local Weather</h2>
<div class="abs" style="left:272px;top:390px">
  <div class="lw-item abs" style="left:0;top:0">
    <div class="icon"><svg width="14" height="12" viewBox="0 0 14 12"><path d="M3 8h8a2.5 2.5 0 0 0 0-5 3.5 3.5 0 0 0-6.6-.6A2.5 2.5 0 0 0 3 8z" fill="#b9d3ea" stroke="#4d8cc6" stroke-width=".8"/><path d="M5 10v1M7 10v1M9 10v1" stroke="#4d8cc6" stroke-width=".8"/></svg></div>
    <div><div class="temp">23 <sup>°</sup> <span class="city">-City Name</span></div><div class="lw-text">Laboris nisi ut aliquip ex ea commodo conseq<br>Duis aute irure dolor reprehenderit...</div></div>
  </div>
  <div class="lw-item abs" style="left:0;top:54px">
    <div class="icon"><svg width="14" height="12" viewBox="0 0 14 12"><circle cx="5" cy="5" r="3" fill="#f6b73c"/><path d="M4 10h7a2.2 2.2 0 0 0 0-4.4 3 3 0 0 0-5.6-.4A2.2 2.2 0 0 0 4 10z" fill="#dbe8f4" stroke="#4d8cc6" stroke-width=".8"/></svg></div>
    <div><div class="temp">23 <sup>°</sup> <span class="city">-City Name</span></div><div class="lw-text">Laboris nisi ut aliquip ex ea commodo conseq<br>Duis aute irure dolor reprehenderit...</div></div>
  </div>
  <div class="lw-item abs" style="left:0;top:108px">
    <div class="icon"><svg width="14" height="12" viewBox="0 0 14 12"><circle cx="5" cy="5" r="3" fill="#f6b73c"/><path d="M4 10h7a2.2 2.2 0 0 0 0-4.4 3 3 0 0 0-5.6-.4A2.2 2.2 0 0 0 4 10z" fill="#dbe8f4" stroke="#4d8cc6" stroke-width=".8"/></svg></div>
    <div><div class="temp">23 <sup>°</sup> <span class="city">-City Name</span></div><div class="lw-text">Laboris nisi ut aliquip ex ea commodo conseq<br>Duis aute irure dolor reprehenderit...</div></div>
  </div>
</div>

<!-- Ad -->
<aside class="abs ad" role="img" aria-label="Advertisement with a dark sports car">
  <div class="abs ad-top">WE LEASE ALL MAKES &amp; MODELS,<br>NEW &amp; USED</div>
  <div class="abs ad-bottom"><b>0%</b> DOWN CAR LEASES ARE BACK</div>
  <div class="abs btn ad-btn">Click Here</div>
</aside>

<!-- Major cities -->
<section class="abs card" style="left:74px;top:562px;width:524px;height:294px"></section>
<div class="abs map" style="left:83px;top:572px;width:505px;height:173px" role="img" aria-label="City map with weather markers"></div>
<h2 class="abs section-title" style="left:83px;top:759px">Weather Forecast of Major Cities</h2>
<div class="abs" style="left:83px;top:776px;width:510px;border-bottom:1px solid var(--line)"></div>
<div class="abs" style="left:83px;top:777px;display:grid;grid-template-columns:repeat(5,107px)">
  <div class="city-cell"><div class="icon"><svg width="14" height="12" viewBox="0 0 14 12"><path d="M3 8h8a2.5 2.5 0 0 0 0-5 3.5 3.5 0 0 0-6.6-.6A2.5 2.5 0 0 0 3 8z" fill="#b9d3ea" stroke="#4d8cc6" stroke-width=".8"/></svg></div><div class="temp">25 <sup>°</sup><span class="city">-City Name</span></div></div>
  <div class="city-cell"><div class="icon"><svg width="14" height="12" viewBox="0 0 14 12"><circle cx="5" cy="5" r="3" fill="#f6b73c"/><path d="M4 10h7a2.2 2.2 0 0 0 0-4.4 3 3 0 0 0-5.6-.4A2.2 2.2 0 0 0 4 10z" fill="#dbe8f4" stroke="#4d8cc6" stroke-width=".8"/></svg></div><div class="temp">30 <sup>°</sup><span class="city">-City Name</span></div></div>
  <div class="city-cell"><div class="icon"><svg width="14" height="12" viewBox="0 0 14 12"><circle cx="5" cy="5" r="3" fill="#f6b73c"/><path d="M4 10h7a2.2 2.2 0 0 0 0-4.4 3 3 0 0 0-5.6-.4A2.2 2.2 0 0 0 4 10z" fill="#dbe8f4" stroke="#4d8cc6" stroke-width=".8"/></svg></div><div class="temp">26 <sup>°</sup><span class="city">-City Name</span></div></div>
  <div class="city-cell"><div class="icon"><svg width="14" height="12" viewBox="0 0 14 12"><path d="M3 8h8a2.5 2.5 0 0 0 0-5 3.5 3.5 0 0 0-6.6-.6A2.5 2.5 0 0 0 3 8z" fill="#f6c56a" stroke="#4d8cc6" stroke-width=".8"/><path d="M5 10v1M8 10v1" stroke="#4d8cc6" stroke-width=".8"/></svg></div><div class="temp">35 <sup>°</sup><span class="city">-City Name</span></div></div>
  <div class="city-cell" style="border-right:0"><div class="icon"><svg width="14" height="12" viewBox="0 0 14 12"><circle cx="6" cy="6" r="3.5" fill="#f6b73c"/><path d="M3 9h8" stroke="#4d8cc6" stroke-width=".8"/></svg></div><div class="temp">38 <sup>°</sup><span class="city">-City Name</span></div></div>
  <div class="city-cell"><div class="icon"><svg width="14" height="12" viewBox="0 0 14 12"><path d="M3 8h8a2.5 2.5 0 0 0 0-5 3.5 3.5 0 0 0-6.6-.6A2.5 2.5 0 0 0 3 8z" fill="#b9d3ea" stroke="#4d8cc6" stroke-width=".8"/></svg></div><div class="temp">21 <sup>°</sup><span class="city">-City Name</span></div></div>
  <div class="city-cell"><div class="icon"><svg width="14" height="12" viewBox="0 0 14 12"><circle cx="5" cy="5" r="3" fill="#f6b73c"/><path d="M4 10h7a2.2 2.2 0 0 0 0-4.4 3 3 0 0 0-5.6-.4A2.2 2.2 0 0 0 4 10z" fill="#dbe8f4" stroke="#4d8cc6" stroke-width=".8"/></svg></div><div class="temp">28 <sup>°</sup><span class="city">-City Name</span></div></div>
  <div class="city-cell"><div class="icon"><svg width="14" height="12" viewBox="0 0 14 12"><circle cx="5" cy="5" r="3" fill="#f6b73c"/><path d="M4 10h7a2.2 2.2 0 0 0 0-4.4 3 3 0 0 0-5.6-.4A2.2 2.2 0 0 0 4 10z" fill="#dbe8f4" stroke="#4d8cc6" stroke-width=".8"/></svg></div><div class="temp">26 <sup>°</sup><span class="city">-City Name</span></div></div>
  <div class="city-cell"><div class="icon"><svg width="14" height="12" viewBox="0 0 14 12"><path d="M3 8h8a2.5 2.5 0 0 0 0-5 3.5 3.5 0 0 0-6.6-.6A2.5 2.5 0 0 0 3 8z" fill="#f6c56a" stroke="#4d8cc6" stroke-width=".8"/><path d="M5 10v1M8 10v1" stroke="#4d8cc6" stroke-width=".8"/></svg></div><div class="temp">32 <sup>°</sup><span class="city">-City Name</span></div></div>
  <div class="city-cell" style="border-right:0"><div class="icon"><svg width="14" height="12" viewBox="0 0 14 12"><circle cx="6" cy="6" r="3.5" fill="#f6b73c"/><path d="M3 9h8" stroke="#4d8cc6" stroke-width=".8"/></svg></div><div class="temp">36 <sup>°</sup><span class="city">-City Name</span></div></div>
</div>
<div class="abs" style="left:83px;top:812px;width:510px;border-bottom:1px solid var(--line)"></div>

<!-- Favorite locations -->
<section class="abs card" style="left:74px;top:867px;width:524px;height:165px"></section>
<h2 class="abs section-title" style="left:74px;top:886px;width:524px;text-align:center">Favorite Locations</h2>
<p class="abs" style="left:74px;top:900px;width:524px;text-align:center;font-size:6.3px;color:#555">Excepteur sint occaecat cupidatat non proident, sunt in culpa qui officia deserunt mollit...</p>
<svg class="abs" style="left:565px;top:886px" width="22" height="10" viewBox="0 0 22 10"><circle cx="5" cy="5" r="4.2" fill="none" stroke="#555" stroke-width=".9"/><path d="M6.5 3 4.5 5l2 2M4.5 5h3" fill="none" stroke="#555" stroke-width=".9"/><circle cx="17" cy="5" r="4.2" fill="none" stroke="#555" stroke-width=".9"/><path d="M15.5 3l2 2-2 2M14.5 5h3" fill="none" stroke="#555" stroke-width=".9"/></svg>
<div class="abs fav-img" style="left:83px;background:linear-gradient(180deg,#8a5a4a,#b86a42 45%,#4c3a35)" role="img" aria-label="Mountain peak at sunset"></div>
<div class="abs fav-img" style="left:213px;background:linear-gradient(180deg,#d9b66a,#4d6a3a 55%,#2d4a2c)" role="img" aria-label="City skyline over a lake"></div>
<div class="abs fav-img" style="left:342px;background:linear-gradient(180deg,#2a5a9c,#9fb5cf 45%,#6b6a3a)" role="img" aria-label="Snowy mountains under blue sky"></div>
<div class="abs fav-img" style="left:473px;background:linear-gradient(180deg,#7a5a3a,#a07040 50%,#4a4a48)" role="img" aria-label="Traveller walking on an autumn road"></div>
<div class="abs fav-cap" style="left:83px">EXCEPTEUR OCCAECAT</div>
<div class="abs fav-cap" style="left:213px">EXCEPTEUR OCCAECAT</div>
<div class="abs fav-cap" style="left:342px">EXCEPTEUR OCCAECAT</div>
<div class="abs fav-cap" style="left:473px">EXCEPTEUR OCCAECAT</div>

<!-- Email signup -->
<section class="abs email">
  <h2 class="abs email-title">EMAIL SIGNUP</h2>
  <p class="abs email-sub">Lorem ipsum dolor sit amet, consectetur adipiscing elit, sed do eiusmod tempor incididunt labore et dolore magna aliqua. Ut enim ad minim veniam, quis..</p>
  <form class="abs email-form">
    <div class="email-field">Enter Email Address</div>
    <div class="btn email-btn">Sign Up Here</div>
  </form>
</section>

<footer>
  <div class="abs" style="left:0;top:1144px;width:672px;height:56px;background:var(--white)"></div>
  <div class="abs footer-links">HOME &nbsp;|&nbsp; WEATHER &nbsp;|&nbsp; MAPS &nbsp;|&nbsp; VIDEOS &nbsp;|&nbsp; PHOTOS &nbsp;|&nbsp; ABOUT &nbsp;|&nbsp; CONTACT</div>
  <div class="abs footer-copy">COPYRIGHTS © SKYVANE , 2017 | ALL RIGHTS RESERVED.</div>
  <div class="abs connect">CONNECT WITH US :</div>
  <div class="abs social" style="left:529px;background:#2f4a8a"></div>
  <div class="abs social" style="left:548px;background:#2aa3e0"></div>
  <div class="abs social" style="left:566px;background:#d9342b"></div>
  <div class="abs social" style="left:584px;background:#9c7a55"></div>
  <div class="abs code">C11</div>
</footer>
</body>
</html>
```